Webdesign für Steuerberaterin
Zielgruppe
Ich bin Steuerberaterin. Meine Zielgruppe sind sowohl Privatpersonen als auch Unternehmer sowie Männer und Frauen.
Aufgabenstellung
Bitte mein Logo und Foto mit berücksichtigen. Ich möchte keine Website, auf der alle 'Reiter' als eine Seite von oben nach unten durchlaufen. Sondern wirklich einzelne, voneinander getrennte Seiten.

```html
<!DOCTYPE html>
<html lang="de">
<head>
<meta charset="utf-8">
<title>Sabine Hortmann – Steuerberaterin</title>
<link href="https://fonts.googleapis.com/css2?family=Ubuntu:wght@400&family=Noto+Sans:wght@400;700&family=Libre+Caslon+Text&display=swap" rel="stylesheet">
<style>
  :root {
    --sidebar: #1b191e;
    --gold: #b58a2a;
    --gold-band: #d8b83c;
    --text: #4a4a4a;
    --brand: #3c3c3c;
    --page: #ffffff;
    --photo-light: #ece9e6;
    --photo-dark: #c9c4bf;
  }
  * { margin: 0; padding: 0; box-sizing: border-box; }
  html, body { width: 1200px; height: 960px; overflow: hidden; background: var(--page); }
  .site { position: relative; width: 1200px; height: 960px; }
  .sidebar { position: absolute; left: 0; top: 0; width: 307px; height: 934px; background: var(--sidebar); }
  .main-nav { position: absolute; left: 80px; top: 300px; list-style: none; font-family: "Ubuntu", sans-serif; font-size: 14px; }
  .main-nav li { height: 45px; }
  .main-nav a { color: var(--gold); text-decoration: none; }
  .portrait {
    position: absolute; left: 194px; top: 320px; width: 401px; height: 289px;
    background: radial-gradient(ellipse at 50% 45%, #f8f7f5 0%, var(--photo-light) 45%, var(--photo-dark) 100%);
  }
  .brand { position: absolute; left: 610px; top: 60px; width: 260px; text-align: center; }
  .brand-mark { display: block; margin: 0 auto 14px; }
  .brand-name { font-family: "Libre Caslon Text", serif; font-size: 22px; color: var(--brand); }
  .brand-role { font-family: "Libre Caslon Text", serif; font-size: 9px; letter-spacing: 2px; color: var(--brand); margin-top: 6px; }
  .content { position: absolute; left: 623px; top: 268px; width: 566px; text-align: center; color: var(--text); font-family: "Noto Sans", sans-serif; }
  .headline { font-family: "Libre Caslon Text", serif; font-weight: 400; font-size: 23px; color: var(--gold); }
  .rule { width: 513px; height: 2px; background: var(--gold); margin: 20px auto 30px 27px; }
  .lead { font-size: 15.5px; font-weight: 700; margin-bottom: 23px; }
  .content p { font-size: 15px; line-height: 22.7px; margin-bottom: 22.7px; }
  .footer-band { position: absolute; left: 0; bottom: 0; width: 1200px; height: 26px; background: linear-gradient(var(--gold-band), #d2ae36); }
</style>
</head>
<body>
<div class="site">
  <aside class="sidebar">
    <ul class="main-nav">
      <li><a href="#">Über mich</a></li>
      <li><a href="#">Leistungen</a></li>
      <li><a href="#">Kontakt</a></li>
      <li><a href="#">Impressum</a></li>
    </ul>
  </aside>
  <div class="portrait" role="img" aria-label="Porträtfoto der Steuerberaterin vor heller Steinwand"></div>
  <header class="brand">
    <svg class="brand-mark" width="14" height="14" viewBox="0 0 14 14"><circle cx="7" cy="7" r="7" fill="#3c3c3c"/></svg>
    <div class="brand-name">Sabine Hortmann</div>
    <div class="brand-role">STEUERBERATERIN</div>
  </header>
  <main class="content">
    <h1 class="headline">Schön, dass Sie da sind</h1>
    <div class="rule"></div>
    <p class="lead">Ich freue mich, dass Sie den Weg zu mir gefunden haben!</p>
    <p>Sie sind bei mir genau richtig:<br>Egal, ob Sie Privatperson sind, die Ihre Einkommensteuer-Erklärung<br>in vertrauensvolle Hände geben möchte,<br>oder Unternehmer, der sich z.B. das „Rundum-Sorglos-Paket“<br>mit Buchführung, Jahresabschluss und Steuererklärungen wünscht.</p>
    <p>Schauen Sie sich hier gerne um und melden Sie sich bei mir – ich bin bei jedem steuerlichen Thema gerne Ihr kompetenter und zuverlässiger Ansprechpartner.</p>
    <p>Für mich ist es eine Selbstverständlichkeit,<br>dass ich auch nach mehr als 12 Jahren Berufserfahrung<br>durch permanente Fortbildungen immer auf dem aktuellsten Stand<br>der relevanten Gesetze und Verordnungen bin.<br>Nur so kann ich Sie bestmöglich beraten.</p>
  </main>
  <div class="footer-band"></div>
</div>
</body>
</html>
```